Mail order Nursery needs banner for promoting perennials that compliment roses.

banner should be 1135 wide x165 tall. We have an existing one displayed but we are not happy with the way it is washed out. Use your creativity to give us something that pops. Would love to see some watercolor or some other form of image other than just words washed across a stock photo. Banner needs to read Perennial Companions for Roses or some variation of that. Colors need to compliment our current theme. You can view the page and banner I want to replace at www.themeadowbellplot.com. The banner we want to replace has been uploaded to the pixel harbor file drop box. Thanks for your help and I look forward to seeing what you guys come up with. EDIT: I don't think I was clear enough in by brief. This banner promotes the sale of plants that look good planted with roses. We are getting to many submissions that are using only roses as the backdrop. We are looking for different types of plants that you would grow in your garden to compliment your roses. Thanks for all your hard work.

Target Market(s)

Home owners between 30 and 65

Industry/Entity Type

Nursery

Colors
33a6d7
e667a6

Requirements
Must have
• Text promotion perennials that compliment roses.... does not have to be those exact words but get the point across
Should not have
• Stock Photos with simple text washed across it.

```html
<!DOCTYPE html>
<html lang="en">
<head>
<meta charset="utf-8">
<title>Perennial Companions for Roses</title>
<link rel="stylesheet" href="https://fonts.googleapis.com/css2?family=Asap+Condensed:wght@600&family=Comfortaa:wght@300&display=swap">
<style>
  :root {
    --paper: #ffffff;
    --title-red: #d42a2e;
    --title-green: #3bab45;
    --theme-blue: #33a6d7;
    --theme-pink: #e667a6;
    --foliage-deep: #2f6a22;
    --foliage-mid: #5f9a2e;
    --foliage-light: #9cc44a;
    --bloom-yellow: #f2dc2a;
    --bloom-red: #e0262a;
  }
  * { margin: 0; padding: 0; box-sizing: border-box; }
  html, body {
    width: 1200px;
    height: 174px;
    overflow: hidden;
    background: var(--paper);
  }
  .banner {
    position: relative;
    width: 1200px;
    height: 174px;
    overflow: hidden;
    background: var(--paper);
  }
  .garden-photo {
    position: absolute;
    top: 0;
    left: 0;
    width: 700px;
    height: 174px;
    background:
      radial-gradient(ellipse 34px 26px at 60px 152px, var(--bloom-red) 60%, transparent 100%),
      radial-gradient(ellipse 22px 18px at 160px 58px, var(--bloom-red) 60%, transparent 100%),
      radial-gradient(ellipse 20px 16px at 222px 104px, var(--bloom-red) 60%, transparent 100%),
      radial-gradient(ellipse 18px 14px at 150px 92px, var(--bloom-red) 60%, transparent 100%),
      radial-gradient(ellipse 26px 20px at 110px 128px, var(--theme-pink) 55%, transparent 100%),
      radial-gradient(ellipse 22px 18px at 290px 150px, var(--theme-pink) 55%, transparent 100%),
      radial-gradient(ellipse 70px 48px at 400px 60px, var(--bloom-yellow) 45%, transparent 100%),
      radial-gradient(ellipse 60px 40px at 330px 120px, var(--bloom-yellow) 45%, transparent 100%),
      radial-gradient(ellipse 50px 34px at 290px 30px, var(--bloom-yellow) 45%, transparent 100%),
      radial-gradient(ellipse 30px 24px at 250px 20px, var(--theme-blue) 50%, transparent 100%),
      radial-gradient(ellipse 26px 20px at 40px 40px, var(--theme-blue) 50%, transparent 100%),
      linear-gradient(180deg, var(--foliage-mid) 0%, var(--foliage-deep) 55%, var(--foliage-light) 100%);
  }
  .title-field {
    position: absolute;
    inset: 0;
    width: 1200px;
    height: 174px;
  }
  .title-field .field { fill: var(--paper); }
  .title-field .edge-blue { fill: none; stroke: var(--theme-blue); stroke-width: 5; }
  .title-field .edge-pink { fill: none; stroke: var(--theme-pink); stroke-width: 3; }
  .headline-main {
    font-family: "Asap Condensed", "Arial Narrow", sans-serif;
    font-weight: 600;
    font-size: 70px;
    fill: var(--title-red);
  }
  .headline-sub {
    font-family: "Comfortaa", "Century Gothic", sans-serif;
    font-weight: 300;
    font-size: 64px;
    fill: var(--title-green);
  }
</style>
</head>
<body>
  <div class="banner">
    <div class="garden-photo" role="img" aria-label="Bright garden border with red and pink tulips, yellow flowering shrubs and blue blooms among green foliage"></div>
    <svg class="title-field" viewBox="0 0 1200 174" role="heading" aria-level="1" aria-label="Perennial Companions For Roses">
      <path class="field" d="M395 0 C 430 70, 560 110, 610 174 L1200 174 L1200 0 Z"/>
      <path class="edge-blue" d="M395 0 C 430 70, 560 110, 610 174"/>
      <path class="edge-pink" d="M384 0 C 419 70, 549 110, 599 174"/>
      <text class="headline-main" x="407" y="74" textLength="767" lengthAdjust="spacingAndGlyphs">Perennial Companions</text>
      <text class="headline-sub" x="640" y="159" textLength="534" lengthAdjust="spacingAndGlyphs">For Roses</text>
    </svg>
  </div>
</body>
</html>
```